Medical VIP club - small design

Please read the specs in a design brief attached. Also we don't have logo in a Vector format and attaching the only version we have.

Industry/Entity Type

Club

```html
<!DOCTYPE html>
<html lang="en">
<head>
<meta charset="utf-8">
<title>Halcyon Club — Comparison of Packages</title>
<link href="https://fonts.googleapis.com/css2?family=Roboto+Condensed:wght@300;400;700&display=swap" rel="stylesheet">
<style>
  :root {
    --bg-dark: #5e4c35;
    --bg-mid: #7a6850;
    --bg-light: #c9c0aa;
    --cream: #f6f3df;
    --cream-soft: #ece9d2;
    --panel: #e3e0c7;
    --frame-dark: #6f5f4a;
    --row: #f4f2e6;
    --ink: #5a4a36;
    --ink-soft: #6d5c47;
    --accent: #8c2a0c;
    --footer-ink: #f2ecdc;
    --brand: #efe8d2;
  }
  * { box-sizing: border-box; margin: 0; padding: 0; }
  html, body { width: 1200px; height: 900px; overflow: hidden; }
  body {
    font-family: "Roboto Condensed", "Arial Narrow", sans-serif;
    color: var(--ink);
    background: linear-gradient(180deg, var(--bg-dark) 0%, var(--bg-mid) 28%, var(--bg-light) 48%, var(--bg-mid) 64%, var(--bg-dark) 82%, var(--bg-dark) 100%);
    position: relative;
  }
  .brand {
    position: absolute; left: 162px; top: 58px; height: 60px;
    display: flex; align-items: center; gap: 14px;
  }
  .brand-mark { width: 26px; height: 26px; background: var(--brand); }
  .brand-name { font-size: 42px; font-weight: 400; color: var(--brand); line-height: 1; }

  .site-panel {
    position: absolute; left: 127px; top: 137px; width: 946px; height: 704px;
    border-radius: 22px; overflow: hidden;
    background: linear-gradient(90deg, #4f3f2c 0%, var(--frame-dark) 4%, #8a7a63 50%, var(--frame-dark) 96%, #4f3f2c 100%);
    box-shadow: 0 4px 14px rgba(0,0,0,.35);
  }
  .main-nav {
    position: absolute; left: 0; top: 0; width: 946px; height: 74px;
    display: flex; background: linear-gradient(180deg, #dcd8bf 0%, var(--cream) 45%, var(--cream-soft) 100%);
  }
  .nav-tab {
    flex: 1; display: flex; align-items: flex-end; justify-content: center; padding-bottom: 14px;
    font-size: 20px; color: var(--ink); text-decoration: none;
    border-left: 1px solid #b9b39a; border-top-left-radius: 28px;
    background: linear-gradient(180deg, #f9f7ea 0%, var(--cream) 100%);
  }
  .nav-tab:first-child { border-left: none; border-top-left-radius: 0; }
  .nav-tab.is-register { color: var(--accent); font-weight: 700; }

  .content-card {
    position: absolute; left: 25px; top: 74px; width: 893px; height: 521px;
    border-radius: 0 0 14px 14px;
    background: linear-gradient(180deg, #d4d0b5 0%, var(--panel) 12%, var(--panel) 100%);
    border: 2px solid #f4f1e2; border-top: none;
  }
  .content-title { position: absolute; left: 53px; top: 42px; font-size: 28px; font-weight: 400; color: var(--ink); }

  .price-row {
    position: absolute; left: 39px; width: 815px; height: 36px;
    display: flex; align-items: center; font-size: 18px; color: var(--ink-soft);
    background: linear-gradient(90deg, #fbfaf2 0%, var(--row) 20%, var(--row) 100%);
  }
  .price-row.is-head { background: #fff; font-size: 21px; color: var(--ink); }
  .price-row.is-total { background: #fff; }
  .cell-item { position: absolute; left: 14px; }
  .cell-desc { position: absolute; left: 141px; }
  .cell-p1 { position: absolute; left: 352px; }
  .cell-p2 { position: absolute; left: 520px; }
  .cell-p3 { position: absolute; left: 689px; }
  .amount { display: inline-flex; width: 88px; justify-content: space-between; }
  .agreement { position: absolute; left: 53px; width: 801px; top: 482px; font-size: 11.5px; color: var(--ink-soft); white-space: nowrap; text-align: justify; text-align-last: justify; }

  .site-footer {
    position: absolute; left: 0; top: 627px; width: 946px; height: 77px;
    background: linear-gradient(180deg, #d8d4bb 0%, var(--cream) 35%, #fbf9ec 60%, var(--cream-soft) 100%);
    display: flex; align-items: center; justify-content: center; gap: 12px; padding-right: 10px;
  }
  .follow-label { font-size: 12.5px; color: var(--ink); }
  .social-link { display: flex; align-items: center; gap: 5px; font-size: 13px; color: var(--ink); text-decoration: none; }
  .social-square { width: 14px; height: 14px; background: var(--ink-soft); border-radius: 3px; }

  .bottom-links {
    position: absolute; top: 850px; left: 0; width: 1200px;
    display: flex; justify-content: center; gap: 16px; font-size: 15px; color: var(--footer-ink);
  }
  .bottom-links a { color: var(--footer-ink); text-decoration: none; }
</style>
</head>
<body>
  <div class="brand">
    <span class="brand-mark"></span>
    <span class="brand-name">Halcyon Club</span>
  </div>

  <div class="site-panel">
    <nav class="main-nav">
      <a class="nav-tab" href="#">About us</a>
      <a class="nav-tab" href="#">VIP Club</a>
      <a class="nav-tab" href="#">Services</a>
      <a class="nav-tab" href="#">Packages @ Prices</a>
      <a class="nav-tab" href="#">Contacs</a>
      <a class="nav-tab is-register" href="#">Registration</a>
    </nav>

    <section class="content-card">
      <h1 class="content-title">Comparison of Packages</h1>

      <div class="price-row is-head" style="top:81px">
        <span class="cell-item">Item</span><span class="cell-desc">Descriptions</span>
        <span class="cell-p1">Package 1</span><span class="cell-p2">Package 2</span><span class="cell-p3">Package 3</span>
      </div>

      <div class="price-row" style="top:131px">
        <span class="cell-item">3</span><span class="cell-desc">Facial Clearance</span>
        <span class="cell-p1 amount"><span>$</span><span>50.00</span></span>
        <span class="cell-p2 amount"><span>$</span><span>300.00</span></span>
        <span class="cell-p3 amount"><span>$</span><span>100.00</span></span>
      </div>
      <div class="price-row" style="top:176px">
        <span class="cell-item">3</span><span class="cell-desc">Facial Clearance</span>
        <span class="cell-p1 amount"><span>$</span><span>50.00</span></span>
        <span class="cell-p2 amount"><span>$</span><span>5.00</span></span>
        <span class="cell-p3 amount"><span>$</span><span>100.00</span></span>
      </div>
      <div class="price-row" style="top:220px">
        <span class="cell-item">3</span><span class="cell-desc">Facial Clearance</span>
        <span class="cell-p1 amount"><span>$</span><span>50.00</span></span>
        <span class="cell-p2 amount"><span>$</span><span>100.00</span></span>
        <span class="cell-p3 amount"><span>$</span><span>100.00</span></span>
      </div>
      <div class="price-row" style="top:265px">
        <span class="cell-item">3</span><span class="cell-desc">Facial Clearance</span>
        <span class="cell-p1 amount"><span>$</span><span>50.00</span></span>
        <span class="cell-p2 amount"><span>$</span><span>100.00</span></span>
        <span class="cell-p3 amount"><span>$</span><span>100.00</span></span>
      </div>
      <div class="price-row" style="top:309px">
        <span class="cell-item">3</span><span class="cell-desc">Facial Clearance</span>
        <span class="cell-p1 amount"><span>$</span><span>50.00</span></span>
        <span class="cell-p2" style="display:inline-flex;gap:12px"><span>$</span><span>FREE</span></span>
        <span class="cell-p3 amount"><span>$</span><span>100.00</span></span>
      </div>
      <div class="price-row" style="top:354px">
        <span class="cell-item">3</span><span class="cell-desc">Facial Clearance</span>
        <span class="cell-p1 amount"><span>$</span><span>50.00</span></span>
        <span class="cell-p2 amount"><span>$</span><span>100.00</span></span>
        <span class="cell-p3 amount"><span>$</span><span>100.00</span></span>
      </div>

      <div class="price-row is-total" style="top:423px">
        <span class="cell-item">Total Amount per Package</span>
        <span class="cell-p1 amount"><span>$</span><span>300.00</span></span>
        <span class="cell-p2 amount"><span>$</span><span>385.00</span></span>
        <span class="cell-p3 amount"><span>$</span><span>600.00</span></span>
      </div>

      <p class="agreement">Agreement: package prices include consultation, transfers and aftercare; rates may vary by clinic and date, please confirm all details with your coordinator before booking.</p>
    </section>

    <footer class="site-footer">
      <span class="follow-label">Follow us on</span>
      <a class="social-link" href="#"><span class="social-square"></span>Chirper</a>
      <a class="social-link" href="#"><span class="social-square"></span>Feedline</a>
      <a class="social-link" href="#"><span class="social-square"></span>Friendbook</a>
    </footer>
  </div>

  <nav class="bottom-links">
    <a href="#">Home</a><span>I</span><a href="#">Services</a><span>I</span><a href="#">About us</a><span>I</span><a href="#">Contact us</a>
  </nav>
</body>
</html>
```